Concept design for a tea business Labels

Hello, we are looking for concepts for our label/packaging for a tea business that has been in business now for over a year. We are a beachy, organic, "It's your moment. Enjoy it." type tea business. We have an online website (www.corvalbrewhouse.com.au) and sell at local markets around the Tarrowby Cove area.
We are looking to upgrade our label to look more professional, in a fun/beachy/chilled out style. (unlike the traditional tea labels).
We do loose leaf tea and iced tea consentrated syrups. We have a few different packages (please see website under "sizes and packaging" bottom left). We would like to experiement with various different size and shape of labels for different products, so would like a concept design for a label using our logo (see website front page bottom). There are no colour constraints.
We use the Quillan brand labels of the following sizes:
1. Pure Glass Rectangular Product Labels, Q4825, 100/Pack, 96 x 50.8 mm
2. Pure Glass Round Multi-purpose Labels, Q3907D, 240/Pack, 40 mm diameter
3.Pure Glass Square Product Labels, Q4861, 350/Pack, 35 x 35 mm
4. For bottles we use Grained Ivory Curved Labels, Q4839, 90/Pack, 57.2 x 77 mm
If you have any more questions, please don't hesitate to contact me
Updates
Hi All,
I am considering using a box like below for packing and doing a bit of a white/beachy feel to the packaging. Either using the rectangle or round circle labels. (circle labels from quillan 60mm diameter).

Reason: Hi All - Thank you so much for all your designs. While I have seen some really beautiful designs I am excited about, it seems there was a rush at the end with a number of new designs just submitted. I still haven't seen just one design I love for the label, so I would like the opportunity to work with some of the new designers to see if we can modify to suit the concept.
Would anyone like to try a concept label with a silhouette of one of the following wave/beach/teacup? I'm just exploring a different approach as I know it is difficult tying in the beach with tea - please think - chilled out beach hut with tea/iced tea, sunrise over ocean. I like the soft colour palette - beachy feel to it - ie. Pastels - blues, greens, whites, sandy, pinks, purples, greys - sunrises over ocean, maybe a white rustic wood feel - or any other icon from Tarrowby Cove - like the Norfolk Pine's along the beach - maybe in Silhouette.
Just some more ideas.
Thank you again for all your contributions!
Petra

```html
<!DOCTYPE html>
<html lang="en">
<head>
<meta charset="utf-8">
<title>Tarrowby Tea Company – Label Concepts</title>
<link rel="stylesheet" href="https://fonts.googleapis.com/css2?family=Yanone+Kaffeesatz:wght@300;400&family=Arvo:wght@400;700&family=Merriweather:wght@400;700&display=swap">
<style>
  :root {
    --lime: #a6ff4d;
    --rose: #ff5a7a;
    --mint: #a3efd2;
    --slate: #4b5068;
    --frame: #9a9db2;
    --paper: #ffffff;
  }
  * { margin: 0; padding: 0; box-sizing: border-box; }
  html, body { width: 1200px; height: 900px; overflow: hidden; background: var(--paper); }
  .sheet { position: relative; width: 1200px; height: 900px; }

  .label { position: absolute; background: var(--paper); border: 1px solid var(--frame); overflow: hidden; }
  .label--rect { left: 169px; width: 544px; height: 288px; }
  .label--square { left: 833px; width: 198px; height: 198px; }

  .band { position: absolute; left: 0; top: 0; width: 544px; height: 115px; }
  .band--lime { fill: var(--lime); }
  .band--rose { fill: var(--rose); }

  .line { position: absolute; left: 0; width: 100%; text-align: center; line-height: 1; white-space: nowrap; }

  .brand-dot { position: absolute; border-radius: 50%; }
  .label--rect .brand-dot { left: 242px; top: 14px; width: 58px; height: 58px; background: var(--paper); }
  .label--square .brand-dot { left: 78px; top: 13px; width: 42px; height: 42px; background: var(--slate); }

  .brand-name { font-family: "Yanone Kaffeesatz", sans-serif; font-weight: 400; letter-spacing: 0.3px; }
  .label--rect .brand-name { top: 78px; font-size: 18px; color: var(--paper); }
  .label--square .brand-name { top: 58px; font-size: 13px; color: var(--slate); }

  .tea-name { font-family: "Yanone Kaffeesatz", sans-serif; font-weight: 300; }
  .label--rect .tea-name { top: 140px; font-size: 58px; }
  .tea-name--lime { color: var(--lime); }
  .tea-name--rose { color: var(--rose); }
  .label--square .tea-name { font-size: 36px; color: var(--mint); line-height: 36px; }

  .organic { font-family: "Arvo", serif; font-weight: 700; color: var(--slate); letter-spacing: 3px; }
  .label--rect .organic { top: 200px; font-size: 19px; }
  .label--square .organic { font-size: 16px; letter-spacing: 2.6px; top: 166px; }

  .web { top: 246px; font-family: "Merriweather", serif; font-weight: 700; font-size: 15px; color: var(--slate); }
  .origin { top: 263px; font-family: "Merriweather", serif; font-weight: 400; font-size: 12.5px; color: var(--slate); }
</style>
</head>
<body>
<main class="sheet">

  <section class="label label--rect" style="top:111px">
    <svg class="band band--lime" viewBox="0 0 544 115" aria-hidden="true">
      <path d="M0 0 V108 q9.7 8 19.43 0 t19.43 0 t19.43 0 t19.43 0 t19.43 0 t19.43 0 t19.43 0 t19.43 0 t19.43 0 t19.43 0 t19.43 0 t19.43 0 t19.43 0 t19.43 0 t19.43 0 t19.43 0 t19.43 0 t19.43 0 t19.43 0 t19.43 0 t19.43 0 t19.43 0 t19.43 0 t19.43 0 t19.43 0 t19.43 0 t19.43 0 t19.43 0 V0 Z"/>
    </svg>
    <span class="brand-dot"></span>
    <p class="line brand-name">TARROWBY TEA COMPANY</p>
    <h2 class="line tea-name tea-name--lime">Buddhas Tears</h2>
    <p class="line organic">ORGANIC</p>
    <p class="line web">www.corvalbrewhouse.com.au</p>
    <p class="line origin">Made in Australia from local and imported ingredients.</p>
  </section>

  <section class="label label--rect" style="top:500px">
    <svg class="band band--rose" viewBox="0 0 544 115" aria-hidden="true">
      <path d="M0 0 V108 q9.7 8 19.43 0 t19.43 0 t19.43 0 t19.43 0 t19.43 0 t19.43 0 t19.43 0 t19.43 0 t19.43 0 t19.43 0 t19.43 0 t19.43 0 t19.43 0 t19.43 0 t19.43 0 t19.43 0 t19.43 0 t19.43 0 t19.43 0 t19.43 0 t19.43 0 t19.43 0 t19.43 0 t19.43 0 t19.43 0 t19.43 0 t19.43 0 t19.43 0 V0 Z"/>
    </svg>
    <span class="brand-dot"></span>
    <p class="line brand-name">TARROWBY TEA COMPANY</p>
    <h2 class="line tea-name tea-name--rose">Wild Rose</h2>
    <p class="line organic">ORGANIC</p>
    <p class="line web">www.corvalbrewhouse.com.au</p>
    <p class="line origin">Made in Australia from local and imported ingredients.</p>
  </section>

  <section class="label label--square" style="top:111px">
    <span class="brand-dot"></span>
    <p class="line brand-name">TARROWBY TEA COMPANY</p>
    <h2 class="line tea-name" style="top:102px">Basil</h2>
    <p class="line organic">ORGANIC</p>
  </section>

  <section class="label label--square" style="top:351px">
    <span class="brand-dot"></span>
    <p class="line brand-name">TARROWBY TEA COMPANY</p>
    <h2 class="line tea-name" style="top:83px">Black<br>Peppercorn</h2>
    <p class="line organic">ORGANIC</p>
  </section>

  <section class="label label--square" style="top:590px">
    <span class="brand-dot"></span>
    <p class="line brand-name">TARROWBY TEA COMPANY</p>
    <h2 class="line tea-name" style="top:83px">Pepper BBQ<br>Herbal Blend</h2>
    <p class="line organic">ORGANIC</p>
  </section>

</main>
</body>
</html>
```